2021 IT Training Presentation Deck Refresh

Copper Lantern is an IT education services firm. We teach IT industry standards and technologies. We are in need of an updated training presentation deck that factors in a fresh take for:

1) Agenda/Table of Contents
2) Chapter Topic Summary
2) Chapter Introduction and Learning Objectives
3) Chapter Recaps
4) Important Point/Pro Tip emphasis
5) Warning Message
6) Mini Quiz layout
7) Lab Exercise Introduction
7) Deck Close Out

Incorporating the official Copper Lantern colour palette for materials that will likely be used in self-paced/online recorded versions of courses.

Target Market(s)

IT

Industry/Entity Type

Computer Training

Requirements
Nice to have
• placeholder sections for images of IT workers in an office or by a computer

```html
<!DOCTYPE html>
<html lang="en">
<head>
<meta charset="utf-8">
<title>Copper Lantern – IT Training Deck Templates</title>
<link href="https://fonts.googleapis.com/css2?family=Outfit:wght@300;400;600;700&family=Roboto:wght@400;500&display=swap" rel="stylesheet">
<style>
:root{
  --navy:#0b0838;
  --ink:#14184a;
  --sky:#cde9f3;
  --mist:#e4f3f9;
  --brand:#4a63c4;
  --s1:#3a4fa6;--s2:#4866b8;--s3:#5b86cc;--s4:#7fb0e0;--s5:#a3d0ee;
  --warn-body:#7b9fd9;
  --page:#ffffff;
}
*{box-sizing:border-box;margin:0;padding:0}
html,body{width:818px;height:1200px;overflow:hidden;background:var(--page)}
body{position:relative;font-family:"Roboto",sans-serif;color:var(--ink)}
.label{position:absolute;width:351px;text-align:center;font-size:14px;color:#111;font-family:"Roboto",sans-serif}
.slide{position:absolute;width:351px;height:197px;overflow:hidden;background:var(--sky);box-shadow:0 3px 8px rgba(0,0,0,.35)}
.col-l{left:43px}.col-r{left:424px}
.row1{top:51px}.row2{top:274px}.row3{top:497px}.row4{top:719px}.row5{top:942px}
.photo{position:absolute}
.brand{position:absolute;font-family:"Outfit",sans-serif;font-weight:300;color:var(--brand);letter-spacing:.3px;white-space:nowrap}
.brand-corner{right:12px;bottom:6px;font-size:7px}
.h-title{position:absolute;font-family:"Outfit",sans-serif;font-weight:700;color:var(--ink);line-height:1.05}
.stripe{position:absolute;height:4px;background:linear-gradient(90deg,var(--s1) 0 20%,var(--s2) 20% 40%,var(--s3) 40% 60%,var(--s4) 60% 80%,var(--s5) 80% 100%)}
.small{font-size:4px;line-height:1.3;color:var(--ink)}
.sub-h{font-family:"Outfit",sans-serif;font-weight:700;font-size:5px;color:var(--ink)}
.bullets{list-style:none}
.bullets li{position:relative;padding-left:5px;margin-bottom:3px}
.bullets li::before{content:"•";position:absolute;left:0}

/* cover */
.cover-photo{inset:0;background:linear-gradient(180deg,#b9ccd8 0%,#9fb6c6 55%,#6d7c86 80%,#4c5a63 100%)}
.cover-mark{position:absolute;left:24px;top:47px;width:92px;height:104px;background:var(--navy)}
.cover-mark .brand{left:0;right:0;text-align:center;top:58px;font-size:8px;color:#7fa4e6}
.cover-panel{position:absolute;left:116px;top:47px;width:211px;height:104px;background:rgba(214,236,246,.82)}
.cover-title{position:absolute;left:16px;top:28px;font-family:"Outfit",sans-serif;font-weight:700;font-size:12.5px;line-height:1.1;color:var(--ink)}
.cover-rule{position:absolute;left:16px;top:58px;width:180px;height:1px;background:var(--ink)}
.cover-sub{position:absolute;left:16px;top:62px;font-size:7.5px;color:var(--ink)}

/* contents */
.contents-photo{left:0;top:0;width:175px;height:197px;background:linear-gradient(180deg,#dfe6ea 0%,#c9d3d8 40%,#3d4a3c 52%,#7e8c96 62%,#4d5c68 100%)}
.contents-h{position:absolute;left:189px;top:64px;font-family:"Outfit",sans-serif;font-weight:600;font-size:10px;color:var(--ink)}
.toc{position:absolute;left:189px;top:80px;list-style:none}
.toc li{display:flex;align-items:center;height:9.1px;font-size:4.5px}
.toc .num{width:10px;height:5px;background:var(--navy);color:#fff;font-size:3.5px;text-align:right;padding-right:1px;line-height:5px;margin-right:5px}

/* summary */
.summary-photo{left:0;top:0;width:351px;height:66px;background:linear-gradient(180deg,#8b97a3 0%,#5e6a76 60%,#3f4a44 100%)}
.summary-list{position:absolute;left:189px;top:82px}
.summary-list ul{list-style:none;border-left:1px solid var(--ink);padding-left:6px;margin-top:4px}
.summary-list li{font-size:4px;height:8.4px}

/* intro */
.intro-photo{right:0;top:0;width:117px;height:197px;background:linear-gradient(180deg,#c7ccd0 0%,#a9b0b5 45%,#5b6670 70%,#3c4a52 100%)}
.intro-col{position:absolute;top:83px;width:88px}
.intro-col p{margin-bottom:3px}
.intro-col .bullets{border-left:1px solid var(--ink);padding-left:3px}

/* recap */
.recap-photo{inset:0;background:linear-gradient(180deg,#eceae6 0%,#e2dfda 55%,#cdb89f 75%,#b8956f 100%)}
.recap-screen{position:absolute;left:138px;top:22px;width:170px;height:110px;background:var(--sky);padding:25px 10px 0 8px}
.recap-screen .brand{font-size:4px;right:6px;bottom:4px}
.recap-title{position:absolute;left:30px;top:48px;font-family:"Outfit",sans-serif;font-weight:700;font-size:10px;line-height:1.1;color:var(--brand);text-align:center}

/* pro tips */
.tips-photo{left:0;top:24px;width:148px;height:148px;background:linear-gradient(135deg,#c9b7a4 0%,#8d7f75 45%,#2c5a93 80%,#1f3f6e 100%)}
.tips-panel{position:absolute;left:148px;top:24px;width:186px;height:148px;background:var(--mist)}
.tips-h{position:absolute;left:14px;top:36px;font-family:"Outfit",sans-serif;font-weight:700;font-size:10px}
.tip{position:absolute;display:flex;gap:4px;width:84px}
.tip svg{flex:none;width:9px;height:9px}

/* warning */
.sign{position:absolute;left:84px;top:27px;width:182px;height:136px;border:3px solid var(--brand);border-radius:12px;overflow:hidden;background:var(--warn-body)}
.sign-head{height:40px;background:var(--navy);color:#8fc4f2;font-family:"Outfit",sans-serif;font-weight:700;font-size:24px;text-align:center;line-height:42px;letter-spacing:1px}
.sign-body{padding:8px 8px 0;text-align:center;font-size:6px;line-height:1.15;color:var(--ink)}
.sign-body p{margin-bottom:4px}
.sign-hazard{position:absolute;left:0;right:0;bottom:0;height:18px;background:repeating-linear-gradient(-60deg,var(--navy) 0 6px,var(--warn-body) 6px 12px)}

/* quiz */
.quiz-photo{inset:0;background:linear-gradient(100deg,#8fa9c4 0%,#b4cbe0 30%,#cde9f3 60%)}
.quiz{position:absolute;left:158px;top:46px;width:150px}
.quiz ol{list-style:none;margin:4px 0 10px 0}
.quiz li{margin-bottom:3.2px}

/* lab */
.lab-photo{left:0;top:0;width:117px;height:197px;background:linear-gradient(180deg,#e9e6dc 0%,#c9c2b0 45%,#5a4a3b 75%,#2e241c 100%)}

/* close */
.close{background:var(--navy)}
.close .brand{left:0;right:0;text-align:center;top:108px;font-size:16px;color:#5d7fd6}
.close-contact{position:absolute;left:0;right:0;top:184px;text-align:center;font-size:4px;color:#5d7fd6;word-spacing:1px}
.close-contact span{margin:0 6px}
</style>
</head>
<body>

<div class="label col-r" style="top:30px">Agenda/Table of Contents</div>
<div class="label col-l" style="top:255px">Chapter Topic Summary</div>
<div class="label col-r" style="top:255px">Chapter Introduction and Learning Objectives</div>
<div class="label col-l" style="top:479px">Chapter Recaps</div>
<div class="label col-r" style="top:479px">Important Point/Pro Tip emphasis</div>
<div class="label col-l" style="top:702px">Warning Message</div>
<div class="label col-r" style="top:702px">Mini Quiz layout</div>
<div class="label col-l" style="top:926px">Lab Exercise Introduction</div>
<div class="label col-r" style="top:926px">Deck Close Out</div>

<!-- Cover -->
<section class="slide col-l row1">
  <div class="photo cover-photo" role="img" aria-label="City skyline across the water under a cloudy sky"></div>
  <div class="cover-mark"><span class="brand">COPPER LANTERN</span></div>
  <div class="cover-panel">
    <h1 class="cover-title">INFORMATION<br>TECHNOLOGY TRAINING</h1>
    <div class="cover-rule"></div>
    <p class="cover-sub">A-Z of Information Technology Solutions</p>
  </div>
</section>

<!-- Contents -->
<section class="slide col-r row1">
  <div class="photo contents-photo" role="img" aria-label="Kayaker on a calm mountain lake with a snowy peak"></div>
  <h2 class="contents-h">Contents</h2>
  <ol class="toc">
    <li><span class="num">1</span>Lorem Ipsum Dolor</li>
    <li><span class="num">2</span>Sit Amet, Consectetuer</li>
    <li><span class="num">3</span>Adipiscing Elit Sed Diam</li>
    <li><span class="num">4</span>Nonummy Nibh Euismod</li>
    <li><span class="num">5</span>Tincidunt Ut Laoreet</li>
    <li><span class="num">6</span>Dolore Magna Aliquam Erat</li>
    <li><span class="num">7</span>Volutpat. Ut Wisi Enim Ad</li>
    <li><span class="num">8</span>Minim Veniam, Quis Nostrud</li>
    <li><span class="num">9</span>Exerci Tation Ullamcorper</li>
    <li><span class="num">10</span>Suscipit Lobortis Nisl Ut Aliquip</li>
  </ol>
  <span class="brand brand-corner">COPPER LANTERN</span>
</section>

<!-- Chapter summary -->
<section class="slide col-l row2">
  <div class="photo summary-photo" role="img" aria-label="City towers along a river"></div>
  <h2 class="h-title" style="left:27px;top:107px;font-size:10px">Ut Wisi Enim Ad Minim<br>Veniam</h2>
  <div class="stripe" style="left:27px;top:132px;width:113px"></div>
  <div class="summary-list">
    <div class="sub-h">CHAPTER TOPIC SUMMARY</div>
    <ul>
      <li>Ipsum Dolor Sit Amet</li>
      <li>Consectetuer Adipiscing</li>
      <li>Elit, Sed Diam Nonummy</li>
      <li>Nibh Euismod Tincidunt Ut Laoreet Dolore</li>
      <li>Magna Aliquam Erat</li>
      <li>Volutpat. Ut Wisi Enim</li>
      <li>Ad Minim Veniam, Quis Nostrud</li>
      <li>Xerci Tation Ullamcorper</li>
      <li>Suscipit Lobortis Nisl Ut Aliquip Ex</li>
      <li>Ea Commodo Consequat</li>
    </ul>
  </div>
  <span class="brand brand-corner">COPPER LANTERN</span>
</section>

<!-- Chapter intro -->
<section class="slide col-r row2">
  <h2 class="h-title" style="left:26px;top:48px;font-size:10px">Ut Wisi Enim Ad Minim Veniam</h2>
  <div class="stripe" style="left:26px;top:62px;width:113px"></div>
  <div class="intro-col small" style="left:26px">
    <div class="sub-h" style="margin-bottom:5px">Introduction</div>
    <p>Ipsum dolor sit amet consectetuer adipiscing elit, sed diam nonummy nibh euismod tincidunt ut laoreet dolore</p>
    <p>Magna aliquam erat volutpat. Ut wisi enim ad minim veniam, quis nostrud exerci tation ullamcorper</p>
    <p>Suscipit lobortis nisl ut aliquip ex ea commodo consequat</p>
    <p>Lorem ipsum dolor sit amet, cons ectetuer adipiscing elit, sed diam nonummy nibh euismod tincidunt ut laoreet dolore magna aliquam.</p>
  </div>
  <div class="intro-col small" style="left:134px">
    <div class="sub-h" style="margin-bottom:5px">Learning Objectives</div>
    <ul class="bullets">
      <li>Ipsum dolor sit amet consectetuer adipiscing elit, sed diam nonummy nibh euismod tincidunt ut laoreet dolore</li>
      <li>Magna aliquam erat volutpat. Ut wisi enim ad minim veniam, quis nostrud exerci tation ullamcorper</li>
      <li>Suscipit lobortis nisl ut aliquip ex ea commodo consequat</li>
      <li>Lorem ipsum dolor sit amet, cons ectetuer adipiscing elit, sed diam nonummy nibh euismod tincidunt ut laoreet dolore magna aliquam.</li>
      <li>Erat volutpat. Ut wisi enim ad minim</li>
    </ul>
  </div>
  <div class="photo intro-photo" role="img" aria-label="Misty city river with towers and a water taxi"></div>
</section>

<!-- Recap -->
<section class="slide col-l row3">
  <div class="photo recap-photo" role="img" aria-label="Laptop on a wooden desk against a pale wall"></div>
  <h2 class="recap-title">Ut Wisi Enim Ad<br>Minim Veniam</h2>
  <div class="recap-screen small">
    <ul class="bullets">
      <li>Ipsum dolor sit amet consectetuer adipiscing elit, sed diam nonummy nibh euismod tincidunt ut laoreet dolore</li>
      <li>Magna aliquam erat volutpat. Ut wisi enim ad minim veniam, quis nostrud exerci tation ullamcorper</li>
      <li>Suscipit lobortis nisl ut aliquip ex ea commodo consequat</li>
      <li>Lorem ipsum dolor sit amet, cons ectetuer adipiscing elit, sed diam nonummy nibh euismod tincidunt ut laoreet dolore magna aliquam.</li>
      <li>Erat volutpat. Ut wisi enim ad minim</li>
    </ul>
    <span class="brand">COPPER LANTERN</span>
  </div>
</section>

<!-- Pro tips -->
<section class="slide col-r row3">
  <div class="photo tips-photo" role="img" aria-label="IT team working on laptops in a modern office by a whiteboard"></div>
  <div class="tips-panel">
    <h2 class="tips-h">PRO TIPS</h2>
    <div class="tip small" style="left:14px;top:56px">
      <svg viewBox="0 0 10 10"><path d="M5 1v8M1.5 5.5 5 4l3.5 1.5M3.5 8.5 5 7.8l1.5.7" stroke="#14184a" stroke-width="1" fill="none"/></svg>
      <span>Ipsum dolor sit amet consectetuer adipiscing elit, sed diam nonummy nibh euismod tincidunt ut laoreet dolore</span></div>
    <div class="tip small" style="left:14px;top:82px">
      <svg viewBox="0 0 10 10"><rect x="1" y="2" width="8" height="6" fill="none" stroke="#14184a"/><path d="M3 2v6M5 2v6M7 2v6" stroke="#14184a" stroke-width=".6"/></svg>
      <span>Magna aliquam erat volutpat. Ut wisi enim ad minim veniam, quis nostrud exerci tation ullamcorper</span></div>
    <div class="tip small" style="left:14px;top:106px">
      <svg viewBox="0 0 10 10"><rect x="1.5" y="3" width="7" height="4" fill="none" stroke="#14184a"/><path d="M3 7v2M7 7v2" stroke="#14184a"/></svg>
      <span>Suscipit lobortis nisl ut aliquip ex ea commodo consequat</span></div>
    <div class="tip small" style="left:96px;top:56px">
      <svg viewBox="0 0 10 10"><circle cx="5" cy="5" r="4" fill="none" stroke="#14184a" stroke-width="1.2"/><circle cx="5" cy="5" r="1.5" fill="#14184a"/></svg>
      <span>Lorem ipsum dolor sit amet, cons ectetuer adipiscing elit, sed diam nonummy nibh euismod tincidunt ut laoreet dolore magna aliquam.</span></div>
    <div class="tip small" style="left:96px;top:82px">
      <svg viewBox="0 0 10 10"><path d="M1 3.5 5 1l4 2.5zM2 4.5v3.5M4 4.5v3.5M6 4.5v3.5M8 4.5v3.5M1 9h8" stroke="#14184a" fill="#14184a" stroke-width=".8"/></svg>
      <span>Erat volutpat. Ut wisi enim ad minim</span></div>
  </div>
  <span class="brand brand-corner">COPPER LANTERN</span>
</section>

<!-- Warning -->
<section class="slide col-l row4">
  <div class="sign">
    <div class="sign-head">WARNING</div>
    <div class="sign-body">
      <p>Ipsum dolor sit amet consectetuer adipiscing elit, sed diam nonummy nibh euismod tincidunt ut laoreet dolore</p>
      <p>Magna aliquam erat volutpat. Ut wisi enim ad minim veniam, quis nostrud exerci tation ullamcorper</p>
      <p>Suscipit lobortis nisl ut aliquip ex ea commodo consequat</p>
    </div>
    <div class="sign-hazard"></div>
  </div>
  <span class="brand brand-corner">COPPER LANTERN</span>
</section>

<!-- Quiz -->
<section class="slide col-r row4">
  <div class="photo quiz-photo" role="img" aria-label="Laptop keyboard and notebook on a desk, faded into blue"></div>
  <div class="quiz small">
    <h2 class="h-title" style="position:static;font-size:10px">MINI QUIZ</h2>
    <div class="stripe" style="position:static;width:133px;height:3px;margin:2px 0 8px"></div>
    <p>Ipsum dolor sit amet consectetuer adipiscing elit, sed diam nonummy nibh euismod tincidunt ut laoreet dolore?</p>
    <ol><li>A.&nbsp; Magna aliquam erat volutpat.</li><li>B.&nbsp; Ut wisi enim ad minim veniam</li><li>C.&nbsp; quis nostrud exerci tation ullamcorper</li><li>D.&nbsp; Suscipit lobortis nisl ut al</li></ol>
    <p>Ipsum dolor sit amet consectetuer adipiscing elit, sed diam nonummy nibh euismod tincidunt ut laoreet dolore?</p>
    <ol><li>A.&nbsp; Magna aliquam erat volutpat.</li><li>B.&nbsp; Ut wisi enim ad minim veniam</li><li>C.&nbsp; quis nostrud exerci tation ullamcorper</li><li>D.&nbsp; Suscipit lobortis nisl ut al</li></ol>
  </div>
  <span class="brand brand-corner">COPPER LANTERN</span>
</section>

<!-- Lab -->
<section class="slide col-l row5">
  <div class="photo lab-photo" role="img" aria-label="Bright computer lab with rows of desks and large windows"></div>
  <h2 class="h-title" style="left:138px;top:48px;font-size:10px">Ut Wisi Enim Ad Minim Veniam</h2>
  <div class="stripe" style="left:138px;top:62px;width:113px"></div>
  <div class="small" style="position:absolute;left:138px;top:83px;width:195px">
    <div class="sub-h" style="margin-bottom:5px">Lab Exercise Introduction</div>
    <p style="margin-bottom:3px">Ipsum dolor sit amet consectetuer adipiscing elit, sed diam nonummy nibh euismod tincidunt ut laoreet dolore</p>
    <p style="margin-bottom:3px">Magna aliquam erat volutpat. Ut wisi enim ad minim veniam, quis nostrud exerci tation ullamcorper</p>
    <p style="margin-bottom:3px">Suscipit lobortis nisl ut aliquip ex ea commodo consequat</p>
    <p>Lorem ipsum dolor sit amet, cons ectetuer adipiscing elit, sed diam nonummy nibh euismod tincidunt ut laoreet dolore magna aliquam.</p>
  </div>
  <span class="brand brand-corner">COPPER LANTERN</span>
</section>

<!-- Close -->
<section class="slide col-r row5 close">
  <span class="brand">COPPER LANTERN</span>
  <p class="close-contact"><span>training@copper-lantern.com</span><span>1-416-555-0142</span><span>www.copper-lantern.com</span></p>
</section>

</body>
</html>
```